Graduation backdrop sign

I need a sign that says
Hey look ma...we made it!.
I want the Hey look ma on one line and in a more blocky font and then the other line of we made it in a more feminine font but something you can read. I am planning to send this file to a printing place to make an acrylic sign. The backdrop color is a bright pink, fuscia and orange colors with gold accent so I am thinking of the background being white with a cute scallop border or a cloud like border. Then make the colors of the fonts be a bright dark pink with orange and gold accents somehow. and maybe a cute but no overwhelming border or accents around the font to make it bright and cheery. I am attaching the backdrop that this will be hung in.

```html
<!DOCTYPE html>
<html lang="en">
<head>
<meta charset="utf-8">
<title>Hey Look Ma… We Made It! – Graduation Backdrop Sign</title>
<link rel="stylesheet" href="https://fonts.googleapis.com/css2?family=Luckiest+Guy&family=Playfair+Display:wght@400&display=swap">
<style>
  :root {
    --backdrop: #e3dfde;
    --shadow: rgba(80, 70, 70, 0.32);
    --sign-white: #ffffff;
    --gold-deep: #cf942c;
    --gold-light: #f6df68;
    --magenta: #cc1285;
    --coral: #e4606c;
    --orange: #f48c3a;
  }
  html, body {
    margin: 0;
    padding: 0;
    width: 1200px;
    height: 960px;
    overflow: hidden;
    background: var(--backdrop);
  }
  .stage {
    position: relative;
    width: 1200px;
    height: 960px;
  }
  .sign-frame {
    position: absolute;
    inset: 0;
  }
  .sign-plate {
    filter: drop-shadow(-12px 20px 14px var(--shadow));
  }
  .floral-accent {
    position: absolute;
    border-radius: 45%;
    background: radial-gradient(ellipse at center, rgba(230, 200, 140, 0.22), rgba(230, 200, 140, 0) 72%);
  }
  .floral-accent--left { left: 92px; top: 408px; width: 212px; height: 312px; }
  .floral-accent--right { left: 920px; top: 432px; width: 192px; height: 292px; }
  .headline {
    position: absolute;
    left: 196px;
    width: 872px;
    top: 326px;
    margin: 0;
    text-align: center;
    white-space: nowrap;
    font-family: "Luckiest Guy", "Arial Black", "Impact", sans-serif;
    font-weight: 900;
    font-size: 118px;
    line-height: 1;
    letter-spacing: -3px;
    text-transform: uppercase;
    background: linear-gradient(90deg, var(--magenta) 4%, var(--orange) 26%, var(--magenta) 40%, var(--coral) 62%, var(--orange) 78%, var(--orange) 88%, var(--magenta) 100%);
    -webkit-background-clip: text;
    background-clip: text;
    color: transparent;
  }
  .tagline {
    position: absolute;
    left: 0;
    width: 1200px;
    top: 424px;
    margin: 0;
    text-align: center;
    font-family: "Playfair Display", "Georgia", serif;
    font-weight: 400;
    font-size: 136px;
    line-height: 1.1;
    letter-spacing: 2px;
    background: linear-gradient(90deg, var(--gold-deep) 25%, var(--gold-light) 48%, var(--gold-deep) 75%);
    -webkit-background-clip: text;
    background-clip: text;
    color: transparent;
  }
  .flourish {
    position: absolute;
    left: 336px;
    top: 626px;
    width: 528px;
    height: 58px;
    border-radius: 50%;
    background: linear-gradient(90deg, var(--orange), var(--magenta) 50%, var(--orange));
    opacity: 0.75;
  }
</style>
</head>
<body>
<div class="stage">
  <svg class="sign-frame" width="1200" height="960" viewBox="0 0 1200 960" aria-hidden="true">
    <defs>
      <linearGradient id="goldBorder" x1="0" y1="0" x2="1" y2="0">
        <stop offset="0" stop-color="#cf942c"/>
        <stop offset="0.45" stop-color="#f6df68"/>
        <stop offset="1" stop-color="#d9a43a"/>
      </linearGradient>
    </defs>
    <path class="sign-plate" fill="var(--sign-white)" stroke="url(#goldBorder)" stroke-width="18" stroke-linejoin="round"
      d="M166 224 H1054 A70 70 0 0 0 1124 294 V662 A70 70 0 0 0 1054 732 H166 A70 70 0 0 0 96 662 V294 A70 70 0 0 0 166 224 Z" />
  </svg>

  <div class="floral-accent floral-accent--left" role="img" aria-label="Fine gold line drawing of lily and tulip blossoms"></div>
  <div class="floral-accent floral-accent--right" role="img" aria-label="Fine gold line drawing of lily and tulip blossoms"></div>

  <h1 class="headline">Hey Look Ma...</h1>
  <p class="tagline">we made it!</p>

  <div class="flourish" role="img" aria-label="Pink and orange scroll flourish divider"></div>
</div>
</body>
</html>
```